Business Card for Beach theme sports bar called TAVRU

I need a business card designed for our employees, front and back. This will be used by the employees of two business locations to hand out to customers. I've attached the previous business cards we used at one time for a Benwicks (it is now Tavru). Looking for a fresh new card that is elegant but has character.

Target Market(s)

30-60, middle class

Contact Information for Business Card

We are a beach bar and sports bar. I am looking for an elegant business card with the front to have the TAVRU logo. Then on the back I need it to allow a space for employees to write their names and for them to write in their schedule. I have attached our old cards with our old name Benwicks so you can pull everything we need on the cards. one thing is missing is we have another location at 2815 N Willow Crest Rd with a number of 702-418-9351. Since we will use it for both locations it should allow the employee to circle or check mark the bar which they work at.

Font styles to use
Sans Serif

Requirements
Must have
• We are looking for some fresh ideas for the business card. Something that will really stick out to customers when the staff hands them out. Creativity will be looked at positively, but we still want it to look upscale and fun.

```html
<!DOCTYPE html>
<html lang="en">
<head>
<meta charset="utf-8">
<title>Tavru Business Card – Front and Back</title>
<link rel="stylesheet" href="https://fonts.googleapis.com/css2?family=Arimo:wght@700&family=Tinos:ital,wght@0,400;1,400&display=swap">
<style>
  :root {
    --page-bg: #d4d4d4;
    --card-light: #f4f5f3;
    --card-dark: #232323;
    --ink: #141414;
    --white: #ffffff;
    --gold: #ffcc00;
    --ghost: #2e2e2e;
  }
  * { margin: 0; padding: 0; box-sizing: border-box; }
  html, body { width: 1200px; height: 1200px; overflow: hidden; }
  body { background: var(--page-bg); position: relative; }

  .card {
    position: absolute;
    left: 250px;
    width: 708px;
    height: 404px;
    overflow: hidden;
  }
  .card-front { top: 144px; background: var(--card-light); }
  .card-back { top: 582px; background: var(--card-dark); color: var(--white); }

  /* Front */
  .brand-name {
    position: absolute;
    left: 0; right: 0; top: 92px;
    text-align: center;
    font-family: "Tinos", serif;
    font-weight: 400;
    font-size: 150px;
    line-height: 1;
    color: var(--ink);
  }
  .tagline {
    position: absolute;
    left: 0; right: 0; top: 315px;
    text-align: center;
    font-family: "Tinos", serif;
    font-size: 34px;
    color: var(--ink);
    letter-spacing: 0.5px;
  }

  /* Back */
  .brand-ghost {
    position: absolute;
    left: 14px; top: 200px;
    font-family: "Tinos", serif;
    font-size: 150px;
    line-height: 1;
    color: var(--ghost);
  }
  .offer-title {
    position: absolute;
    left: 0; right: 0; top: 22px;
    text-align: center;
    font-family: "Arimo", sans-serif;
    font-weight: 700;
    font-size: 82px;
    line-height: 1;
    color: var(--gold);
    letter-spacing: 0.5px;
  }
  .field-label {
    position: absolute;
    left: 38px; top: 116px;
    font-family: "Arimo", sans-serif;
    font-weight: 700;
    font-size: 35px;
    line-height: 1;
    letter-spacing: 0.5px;
  }
  .name-box {
    position: absolute;
    left: 40px; top: 166px;
    width: 223px; height: 57px;
    border: 3px solid var(--white);
  }
  .schedule {
    position: absolute;
    left: 311px; top: 142px;
    width: 354px;
  }
  .schedule-days, .schedule-boxes { display: flex; }
  .schedule-days span {
    flex: 1;
    text-align: center;
    font-family: "Arimo", sans-serif;
    font-weight: 700;
    font-size: 24px;
    line-height: 1;
    height: 31px;
  }
  .schedule-boxes span {
    flex: 1;
    height: 43px;
    border: 3px solid var(--white);
    margin-right: 1px;
  }
  .schedule-boxes span:last-child { margin-right: 0; }

  .location {
    position: absolute;
    font-family: "Tinos", serif;
    font-size: 21px;
    line-height: 27px;
    text-align: center;
  }
  .location-north { left: 60px; width: 240px; top: 271px; }
  .location-harbor { left: 396px; width: 280px; top: 258px; }

  .fine-print {
    position: absolute;
    left: 0; right: 0; top: 367px;
    text-align: center;
    font-family: "Tinos", serif;
    font-style: italic;
    font-size: 11.5px;
  }
</style>
</head>
<body>
  <section class="card card-front" aria-label="Card front">
    <div class="brand-name">Tavru</div>
    <div class="tagline">A Gamers Bar</div>
  </section>

  <section class="card card-back" aria-label="Card back">
    <div class="brand-ghost" aria-hidden="true">Tavru</div>
    <h1 class="offer-title">$20 MATCH PLAY</h1>

    <div class="field-label">Bartender</div>
    <div class="name-box"></div>

    <div class="schedule">
      <div class="schedule-days">
        <span>M</span><span>T</span><span>W</span><span>Th</span><span>F</span><span>Sa</span><span>Su</span>
      </div>
      <div class="schedule-boxes">
        <span></span><span></span><span></span><span></span><span></span><span></span><span></span>
      </div>
    </div>

    <address class="location location-north" style="font-style:normal">
      2815 N Willow Crest Rd<br>702-418-9351
    </address>
    <address class="location location-harbor" style="font-style:normal">
      3460 W Harbor Point Rd<br>Las Vegas, NV 89147<br>702-563-1184<br>cs@tavrubar.com
    </address>

    <p class="fine-print">Match play for new slot members, must play total 100 coin.&nbsp; Please see bartender for details.&nbsp; Management reserves all rights</p>
  </section>
</body>
</html>
```